Kelvo Tech Oz Business card revamp

We are looking to revamp our business card design. We are hoping to change our colours to dark navey blue, gray, white and black but are open to keeping the same if a good design is submited. We are after somthing a bit differnt not just boring business card. I have attached a copy of our current card. We Want to keep the same logo design which i have attached a few to hopfully help you in this process. We are after a design that can be personalized to separate 4 people

Colors
0455a3
ffffff
000000
cbcbcb

Requirements
Must have
• Kelvo Tech Logo, address 3/41 Mallory Court, Wexhill 4218, phone number, Name and position

```html
<!DOCTYPE html>
<html lang="en">
<head>
<meta charset="utf-8">
<title>Kelvo Tech Oz – Business Card</title>
<link rel="stylesheet" href="https://fonts.googleapis.com/css2?family=Open+Sans:wght@400;600;700&display=swap">
<style>
  :root {
    --page-bg: #1c1c1d;
    --card-bg: #262628;
    --brand-blue: #2f7fd0;
    --brand-orange: #e07233;
    --text-white: #ffffff;
    --text-soft: #e6e6e6;
    --rule-gray: #cbcbcb;
  }
  * { box-sizing: border-box; margin: 0; padding: 0; }
  html, body {
    width: 1200px; height: 716px; overflow: hidden;
    background: var(--page-bg);
    font-family: "Open Sans", Arial, sans-serif;
  }
  .stage {
    position: relative; width: 1200px; height: 716px;
    display: flex; align-items: center; justify-content: center; gap: 50px;
  }
  .card {
    position: relative; width: 530px; height: 303px;
    background: var(--card-bg); border-radius: 18px; overflow: hidden;
    box-shadow: 0 14px 30px rgba(0,0,0,.55);
  }

  /* Front */
  .card-front { display: flex; flex-direction: column; align-items: center; justify-content: center; }
  .brand { display: flex; align-items: center; gap: 12px; }
  .brand-dot { width: 34px; height: 34px; border-radius: 50%; background: var(--brand-blue); }
  .brand-name { font-weight: 700; font-size: 50px; color: var(--brand-blue); letter-spacing: -1px; line-height: 1; }
  .brand-tagline { margin-top: 8px; font-weight: 700; font-size: 17px; color: var(--brand-blue); letter-spacing: .5px; }
  .front-url { margin-top: 38px; font-size: 15px; color: var(--brand-orange); }

  /* Back */
  .name-block { position: absolute; left: 34px; top: 30px; padding-left: 18px; }
  .name-block::before {
    content: ""; position: absolute; left: 0; top: 2px; width: 8px; height: 46px; background: var(--brand-blue);
  }
  .person-name { font-size: 26px; color: var(--text-white); line-height: 1.1; }
  .person-name strong { font-weight: 700; }
  .job-title { font-size: 14px; color: var(--brand-blue); }
  .rule-gray { position: absolute; left: 34px; top: 96px; width: 250px; height: 3px; background: var(--rule-gray); }
  .rule-blue { position: absolute; left: 284px; top: 96px; width: 246px; height: 3px; background: var(--brand-blue); }
  .back-brand { position: absolute; right: 28px; top: 30px; text-align: right; }
  .back-brand .brand-name { font-size: 30px; }
  .back-brand .brand-dot { width: 20px; height: 20px; }
  .back-brand .brand-tagline { font-size: 11px; margin-top: 4px; }
  .contact-list { position: absolute; left: 34px; top: 126px; list-style: none; }
  .contact-item { display: flex; align-items: center; gap: 12px; font-size: 15px; color: var(--text-soft); margin-bottom: 9px; }
  .contact-item svg { width: 16px; height: 16px; fill: var(--brand-blue); flex: none; }
  .footer-band {
    position: absolute; left: 0; right: 0; bottom: 0; height: 74px; background: var(--brand-orange);
    display: flex; align-items: center; padding-left: 34px;
  }
  .footer-url { font-size: 16px; color: var(--text-white); }
</style>
</head>
<body>
<main class="stage">
  <section class="card card-front" aria-label="Card front">
    <div class="brand">
      <span class="brand-dot"></span>
      <span class="brand-name">Kelvo Tech</span>
    </div>
    <p class="brand-tagline">Passive Fire Protection</p>
    <p class="front-url">www.kelvotech.com.au</p>
  </section>

  <section class="card card-back" aria-label="Card back">
    <div class="name-block">
      <p class="person-name">Your <strong>Name</strong></p>
      <p class="job-title">Job Title</p>
    </div>
    <div class="back-brand">
      <div class="brand">
        <span class="brand-dot"></span>
        <span class="brand-name">Kelvo Tech</span>
      </div>
      <p class="brand-tagline">Passive Fire Protection</p>
    </div>
    <div class="rule-gray"></div>
    <div class="rule-blue"></div>
    <ul class="contact-list">
      <li class="contact-item">
        <svg viewBox="0 0 16 16"><path d="M3 1h3l1.5 4-2 1.2a9 9 0 0 0 4.3 4.3L11 8.5l4 1.5v3a2 2 0 0 1-2 2A12 12 0 0 1 1 3a2 2 0 0 1 2-2z"/></svg>
        07 5550 1842
      </li>
      <li class="contact-item">
        <svg viewBox="0 0 16 16"><path d="M1 3h14v10H1z M1.5 3.5 8 9l6.5-5.5" stroke="#262628" stroke-width="1.2"/></svg>
        youremail@xyz.com
      </li>
      <li class="contact-item">
        <svg viewBox="0 0 16 16"><path d="M8 0a5.5 5.5 0 0 0-5.5 5.5C2.5 10 8 16 8 16s5.5-6 5.5-10.5A5.5 5.5 0 0 0 8 0zm0 8a2.5 2.5 0 1 1 0-5 2.5 2.5 0 0 1 0 5z"/></svg>
        3/41 Mallory Court, Wexhill
      </li>
    </ul>
    <div class="footer-band">
      <p class="footer-url">www.kelvotech.com.au</p>
    </div>
  </section>
</main>
</body>
</html>
```